Veltiwell- Comprehensive quality healthcare delivered at your door.

I am looking for brochures to help promote my business. My business name is Veltiwel (see attachment and logo). This is a new health delivery system designed to provide high quality care to elderly in their communities or at home.

See attachements. The logo is already designed.

As far as services provided (see attachment)

Target Market(s)

Elderly patients

Industry/Entity Type

Business

Font styles to use
Serif

Colors

Designer to choose colors to be used in the design.

```html
<!DOCTYPE html>
<html lang="en">
<head>
<meta charset="utf-8">
<title>Veltiwel Tri-fold Brochure</title>
<link rel="stylesheet" href="https://fonts.googleapis.com/css2?family=Marcellus&family=Lato:wght@400;700&display=swap">
<style>
  :root {
    --forest: #1f2e06;
    --orange: #f39b16;
    --paper: #ffffff;
    --panel-grey: #eeeeee;
    --ink: #2a2a2a;
    --backdrop: #9a9a9a;
  }
  * { margin: 0; padding: 0; box-sizing: border-box; }
  html, body { width: 1200px; height: 1200px; overflow: hidden; background: var(--backdrop); }
  .brochure {
    position: absolute; left: 0; top: 172px; width: 1200px; height: 856px;
    background: var(--paper); overflow: hidden;
    font-family: "Lato", sans-serif; color: var(--ink);
  }
  .brochure-art { position: absolute; inset: 0; }
  .stay-home {
    position: absolute; left: 39px; top: 33px; padding: 0 6px; height: 18px; line-height: 18px;
    background: var(--forest); color: #fff; border-radius: 9px; font-size: 14px; font-weight: 700;
  }
  .intro {
    position: absolute; left: 39px; width: 345px; font-size: 13px; line-height: 16.6px; text-align: justify;
  }
  .intro-first { top: 58px; }
  .intro-second { top: 125px; }
  .service-list { position: absolute; left: 39px; top: 222px; list-style: none; font-size: 13px; line-height: 16.6px; }
  .service-list li::before { content: "•"; color: var(--orange); margin-right: 6px; font-size: 11px; }
  .brand-mark { position: absolute; border-radius: 50%; background: var(--orange); border: 3px solid var(--forest); }
  .brand-mark-small { left: 567px; top: 348px; width: 64px; height: 64px; }
  .brand-mark-large { left: 936px; top: 472px; width: 122px; height: 122px; }
  .brand-name { position: absolute; font-family: "Marcellus", serif; color: var(--forest); text-align: center; }
  .brand-name-small { left: 470px; width: 260px; top: 416px; font-size: 19px; }
  .brand-name-large { left: 830px; width: 334px; top: 595px; font-size: 36px; }
  .contact-item { position: absolute; left: 430px; width: 340px; text-align: center; font-size: 13.5px; }
  .contact-icon { position: absolute; left: 592px; width: 18px; height: 18px; }
  .tagline {
    position: absolute; left: 820px; width: 354px; top: 637px; text-align: center;
    font-family: "Marcellus", serif; color: var(--orange); font-size: 39px; line-height: 44px;
  }
  .tagline-strong {
    position: absolute; left: 820px; width: 354px; top: 668px; text-align: center;
    font-family: "Marcellus", serif; color: var(--forest); font-size: 86px; line-height: 100px;
  }
  .web-address {
    position: absolute; left: 820px; width: 354px; top: 804px; text-align: center;
    font-size: 15px; letter-spacing: 3px; color: var(--ink);
  }
</style>
</head>
<body>
<main class="brochure">
  <svg class="brochure-art" viewBox="0 0 865 617" width="1200" height="856" preserveAspectRatio="none">
    <defs>
      <linearGradient id="panelShade" x1="0" x2="1">
        <stop offset="0" stop-color="#f2f2f2"/><stop offset="0.5" stop-color="#ffffff"/><stop offset="1" stop-color="#eeeeee"/>
      </linearGradient>
      <linearGradient id="gardenTones" x1="0" y1="0" x2="0" y2="1">
        <stop offset="0" stop-color="#7f9a6a"/><stop offset="0.5" stop-color="#a9b7c6"/><stop offset="1" stop-color="#8a6f55"/>
      </linearGradient>
      <linearGradient id="careTones" x1="0" y1="0" x2="1" y2="1">
        <stop offset="0" stop-color="#d9c7b4"/><stop offset="0.6" stop-color="#efe6dc"/><stop offset="1" stop-color="#d8cfc8"/>
      </linearGradient>
      <clipPath id="leftPanel"><rect x="0" y="0" width="286" height="617"/></clipPath>
      <clipPath id="innerPanels"><rect x="230" y="0" width="635" height="617"/></clipPath>
      <clipPath id="wholeSheet"><rect x="0" y="0" width="865" height="617"/></clipPath>
    </defs>
    <rect class="panel-centre" x="286" y="0" width="295" height="617" fill="url(#panelShade)"/>
    <rect class="panel-cover" x="581" y="0" width="284" height="617" fill="#f7f7f7"/>
    <line x1="286" y1="0" x2="286" y2="617" stroke="#e2e2e2"/>
    <line x1="581" y1="0" x2="581" y2="617" stroke="#e2e2e2"/>

    <g class="bottom-wave" clip-path="url(#innerPanels)">
      <circle cx="432" cy="720" r="200" fill="var(--orange)"/>
      <circle cx="440" cy="728" r="192" fill="var(--forest)"/>
    </g>
    <g class="left-photo-frame" clip-path="url(#leftPanel)">
      <circle cx="162" cy="481" r="190" fill="var(--forest)"/>
      <circle cx="182" cy="489" r="150" fill="var(--orange)"/>
      <g role="img" aria-label="Photo: smiling senior in a wheelchair with a caregiver in a garden">
        <circle cx="192" cy="486" r="132" fill="url(#gardenTones)"/>
      </g>
    </g>
    <g class="cover-photo-frame" clip-path="url(#wholeSheet)">
      <circle cx="450" cy="-90" r="180" fill="var(--orange)"/>
      <circle cx="445" cy="-98" r="174" fill="var(--forest)"/>
      <circle cx="722" cy="146" r="178" fill="var(--forest)"/>
      <circle cx="702" cy="140" r="140" fill="var(--orange)"/>
      <g role="img" aria-label="Photo: nurse caring for an elderly woman">
        <circle cx="692" cy="142" r="126" fill="url(#careTones)"/>
      </g>
    </g>
  </svg>

  <span class="stay-home">STAY HOME</span>
  <p class="intro intro-first">Veltiwel offers home and Community Based Services for adults who wish to continue to live independently in the comfort of their communities.</p>
  <p class="intro intro-second">We provide on site services and deliver high quality healthcare at your door. Our experienced physicians co-ordinate care with our certified nurse practitioners and provide chronic care management, physical therapy, rehabilitation and medications management.</p>
  <ul class="service-list">
    <li>Home</li>
    <li>Assisted Living</li>
    <li>Skilled Nursing</li>
    <li>Independent Living</li>
    <li>Home and Community Based Services</li>
    <li>Respite Care</li>
    <li>Rehabilitation</li>
    <li>Mindra LearningCenter</li>
    <li>Mindra Learning®</li>
  </ul>

  <span class="brand-mark brand-mark-small"></span>
  <span class="brand-name brand-name-small">VELTIWEL</span>

  <svg class="contact-icon" style="top:488px" viewBox="0 0 18 18"><circle cx="9" cy="9" r="7.5" fill="none" stroke="var(--orange)" stroke-width="1.4"/><path d="M6 5.5l1.5-.5 1 2-1 .8a5 5 0 0 0 2.2 2.2l.8-1 2 1-.5 1.5c-3 .3-6.3-3-6-6z" fill="var(--orange)"/></svg>
  <p class="contact-item" style="top:513px">your ph no.goes here</p>
  <svg class="contact-icon" style="top:537px" viewBox="0 0 18 18"><circle cx="9" cy="9" r="7.5" fill="var(--orange)"/><ellipse cx="9" cy="9" rx="3" ry="5.5" fill="none" stroke="#fff" stroke-width="1"/><line x1="3.5" y1="9" x2="14.5" y2="9" stroke="#fff" stroke-width="1"/></svg>
  <p class="contact-item" style="top:561px">www.Veltiwel.com</p>
  <svg class="contact-icon" style="top:585px" viewBox="0 0 18 18"><circle cx="9" cy="9" r="7.5" fill="var(--orange)"/><rect x="5" y="6" width="8" height="6" fill="#fff"/><path d="M5 6l4 3.5L13 6" fill="none" stroke="var(--orange)" stroke-width="1"/></svg>
  <p class="contact-item" style="top:609px">your e-mail adress goes here</p>
  <svg class="contact-icon" style="top:633px" viewBox="0 0 18 18"><circle cx="9" cy="9" r="7.5" fill="none" stroke="var(--orange)" stroke-width="1.4"/><path d="M9 14s-3-3.5-3-6a3 3 0 0 1 6 0c0 2.5-3 6-3 6z" fill="var(--orange)"/><circle cx="9" cy="8" r="1" fill="#fff"/></svg>
  <p class="contact-item" style="top:657px">Lorem Ipsum is simply dummy text</p>

  <span class="brand-mark brand-mark-large"></span>
  <span class="brand-name brand-name-large">VELTIWEL</span>
  <p class="tagline">CARING FOR YOU</p>
  <p class="tagline-strong">For life</p>
  <p class="web-address">www.veltiwel.com</p>
</main>
</body>
</html>
```